Infografiken für Unternehmensberatung zu Automatisierung und Digitalisierung
LRPT
Tolle Arbeit in kurzer Zeit fertigestellt. Zügige Kommunikation, Umsetzung und Anpassungen. Ich bin sehr zufrieden und kann Lady Corntwig mit einem gutem Gefühl weiterempfehlen. Danke
Zielgruppe
Unternehmensberatung zu Automatisierung und Digitalisierung
Aufgabenstellung
Hochwertiges und ansprechendes Design der Beratungsprozesse. Grafik soll in verschiedene Größen eingesetzt und farblich auf das CI der Website/Logos abgestimmt sein.
Gerne kann zwischen den drei Kreisen etwas Raum sein oder der äußere Kreis aus einzelnen Feldern bestehen. Die Beschriftung soll an den Kreisradius angepasst werden. Das copyright bitte auch an den Radius des Kreis anpassen.

```html
<!DOCTYPE html>
<html lang="de">
<head>
<meta charset="utf-8">
<title>Systemlösung – Brennwald Partner GmbH</title>
<link rel="stylesheet" href="https://fonts.googleapis.com/css2?family=Fira+Sans:wght@400;500;600;700;800&display=swap">
<style>
  :root {
    --brand-blue: #1f4785;
    --ink: #1a1a1a;
    --muted-grey: #bdbdbd;
    --paper: #ffffff;
  }
  html, body {
    margin: 0;
    padding: 0;
    width: 849px;
    height: 1200px;
    overflow: hidden;
    background: var(--paper);
  }
  .sheet {
    position: relative;
    width: 849px;
    height: 1200px;
    font-family: "Fira Sans", sans-serif;
  }
  .sheet svg { display: block; }
  .title {
    font-weight: 800;
    font-size: 44px;
    letter-spacing: 9px;
    fill: var(--brand-blue);
  }
  .firm-name {
    font-weight: 600;
    font-size: 22px;
    letter-spacing: 2px;
    fill: var(--muted-grey);
  }
  .segment { fill: var(--brand-blue); }
  .segment-gap { stroke: var(--paper); stroke-width: 6; }
  .spoke { stroke: var(--ink); stroke-width: 3.5; }
  .core { fill: var(--ink); }
  .ring-label {
    font-size: 25px;
    font-weight: 400;
    fill: var(--paper);
  }
  .inner-label {
    font-size: 21px;
    font-weight: 400;
    fill: var(--ink);
  }
  .core-label {
    font-size: 26px;
    font-weight: 400;
    fill: var(--paper);
  }
  .copyright {
    font-size: 14px;
    letter-spacing: 1.6px;
    fill: var(--ink);
  }
</style>
</head>
<body>
<main class="sheet">
  <svg width="849" height="1200" viewBox="0 0 849 1200" xmlns="http://www.w3.org/2000/svg">
    <!-- Header -->
    <text class="title" x="429" y="128" text-anchor="middle">SYSTEMLÖSUNG</text>
    <text class="firm-name" x="425" y="157" text-anchor="middle">Brennwald Partner GmbH</text>

    <!-- Process wheel -->
    <g class="wheel" transform="translate(425 586)">
      <defs>
        <path id="segment-shape" d="M0,-305 A305,305 0 0 1 264.1,-152.5 L147.2,-85 A170,170 0 0 0 0,-170 L0,-198 L32,-239 L0,-282 Z"/>
        <path id="arc-strategy" d="M-76.95,-211.5 A225,225 0 0 1 221.6,-39.1"/>
        <path id="arc-audience-outer" d="M155.6,-185.4 A242,242 0 0 1 155.6,185.4"/>
        <path id="arc-audience-inner" d="M131.2,-156.3 A204,204 0 0 1 131.2,156.3"/>
        <path id="arc-inform-outer" d="M238.4,42.1 A242,242 0 0 1 -82.8,227.5"/>
        <path id="arc-inform-inner" d="M200.9,35.5 A204,204 0 0 1 -69.8,191.8"/>
        <path id="arc-marketing-outer" d="M82.8,227.5 A242,242 0 0 1 -238.4,42.1"/>
        <path id="arc-marketing-inner" d="M69.8,191.8 A204,204 0 0 1 -200.9,35.5"/>
        <path id="arc-sales-outer" d="M-155.6,185.4 A242,242 0 0 1 -155.6,-185.4"/>
        <path id="arc-sales-inner" d="M-131.2,156.3 A204,204 0 0 1 -131.2,-156.3"/>
        <path id="arc-team-outer" d="M-238.4,-42.1 A242,242 0 0 1 82.8,-227.5"/>
        <path id="arc-team-inner" d="M-200.9,-35.5 A204,204 0 0 1 69.8,-191.8"/>
        <path id="arc-automate-outer" d="M-98.3,-68.8 A120,120 0 0 1 98.3,-68.8"/>
        <path id="arc-automate-inner" d="M-79.5,-55.6 A97,97 0 0 1 79.5,-55.6"/>
        <path id="arc-scale-outer" d="M108.8,-50.7 A120,120 0 0 1 10.5,119.5"/>
        <path id="arc-scale-inner" d="M87.9,-41 A97,97 0 0 1 8.5,96.6"/>
        <path id="arc-expert-outer" d="M-10.5,119.5 A120,120 0 0 1 -108.8,-50.7"/>
        <path id="arc-expert-inner" d="M-8.5,96.6 A97,97 0 0 1 -87.9,-41"/>
      </defs>

      <g class="outer-ring">
        <use href="#segment-shape" class="segment"/>
        <use href="#segment-shape" class="segment" transform="rotate(60)"/>
        <use href="#segment-shape" class="segment" transform="rotate(120)"/>
        <use href="#segment-shape" class="segment" transform="rotate(180)"/>
        <use href="#segment-shape" class="segment" transform="rotate(240)"/>
        <use href="#segment-shape" class="segment" transform="rotate(300)"/>
      </g>

      <g class="segment-gaps">
        <line class="segment-gap" x1="0" y1="-310" x2="0" y2="-166"/>
        <line class="segment-gap" x1="268.5" y1="-155" x2="143.8" y2="-83"/>
        <line class="segment-gap" x1="268.5" y1="155" x2="143.8" y2="83"/>
        <line class="segment-gap" x1="0" y1="310" x2="0" y2="166"/>
        <line class="segment-gap" x1="-268.5" y1="155" x2="-143.8" y2="83"/>
        <line class="segment-gap" x1="-268.5" y1="-155" x2="-143.8" y2="-83"/>
      </g>

      <g class="ring-labels">
        <text class="ring-label"><textPath href="#arc-strategy" startOffset="50%" text-anchor="middle">Strategie</textPath></text>
        <text class="ring-label"><textPath href="#arc-audience-outer" startOffset="50%" text-anchor="middle">Eindeutige</textPath></text>
        <text class="ring-label"><textPath href="#arc-audience-inner" startOffset="50%" text-anchor="middle">Zielgruppe</textPath></text>
        <text class="ring-label"><textPath href="#arc-inform-outer" startOffset="50%" text-anchor="middle">Systematisch</textPath></text>
        <text class="ring-label"><textPath href="#arc-inform-inner" startOffset="50%" text-anchor="middle">informieren</textPath></text>
        <text class="ring-label"><textPath href="#arc-marketing-outer" startOffset="50%" text-anchor="middle">Magnet-</textPath></text>
        <text class="ring-label"><textPath href="#arc-marketing-inner" startOffset="50%" text-anchor="middle">Marketing</textPath></text>
        <text class="ring-label"><textPath href="#arc-sales-outer" startOffset="50%" text-anchor="middle">Verkaufen</textPath></text>
        <text class="ring-label"><textPath href="#arc-sales-inner" startOffset="50%" text-anchor="middle">&amp; betrachten</textPath></text>
        <text class="ring-label"><textPath href="#arc-team-outer" startOffset="50%" text-anchor="middle">Team bilden</textPath></text>
        <text class="ring-label"><textPath href="#arc-team-inner" startOffset="50%" text-anchor="middle">&amp; entwicklen</textPath></text>
      </g>

      <g class="inner-ring">
        <line class="spoke" x1="66.7" y1="-38.5" x2="147.2" y2="-85"/>
        <line class="spoke" x1="-66.7" y1="-38.5" x2="-147.2" y2="-85"/>
        <line class="spoke" x1="0" y1="77" x2="0" y2="170"/>
        <text class="inner-label"><textPath href="#arc-automate-outer" startOffset="50%" text-anchor="middle">Automatisieren</textPath></text>
        <text class="inner-label"><textPath href="#arc-automate-inner" startOffset="50%" text-anchor="middle">&amp; Digitalisieren</textPath></text>
        <text class="inner-label"><textPath href="#arc-scale-outer" startOffset="50%" text-anchor="middle">Unternehmen</textPath></text>
        <text class="inner-label"><textPath href="#arc-scale-inner" startOffset="50%" text-anchor="middle">skalieren</textPath></text>
        <text class="inner-label"><textPath href="#arc-expert-outer" startOffset="50%" text-anchor="middle">Experten</textPath></text>
        <text class="inner-label"><textPath href="#arc-expert-inner" startOffset="50%" text-anchor="middle">positionierung</textPath></text>
      </g>

      <g class="core-goal">
        <circle class="core" r="77"/>
        <text class="core-label" text-anchor="middle">
          <tspan x="0" y="-20">Zeit &amp;</tspan>
          <tspan x="0" y="4">Lebens-</tspan>
          <tspan x="0" y="29">qualität</tspan>
        </text>
      </g>
    </g>

    <!-- Footer -->
    <text class="copyright" x="425" y="1161" text-anchor="middle">Copyright© Brennwald Partner GmbH | www.brennwald-partner.de</text>
  </svg>
</main>
</body>
</html>
```